vellar.com music website

I need a graphic designer to help me design a very modern looking theme for vellar.com, a website for sharing songs. I currently have a very ugly old-looking design that I want to replace. I need a great logo, a great page theme. Just one comp is all I need of the home page. Must have two tag lines: "it pays to share" and "get paid to share music" The current design has all the elements I need, so I have attached it as a download. vellar is pronounced vehlar. the current site is not live. Please feel free to send me questions.
Updates

Reason: I want to give everyone a chance to get their design in. Thank you.

Target Market(s)

The site needs to appeal to music fans that will be pulled in by the concept of "it pays to share," as well as the pop of the design. It has to look fun and cool. Empahsis on modern looking design.

Industry/Entity Type

Graphic Designer

Requirements
Must have
• engaging logo, there must be a container that holds video, scrolls right and left. 6 action buttons, for Plumora, Zendrol, My, Add, Search, More. You can put the first letter only on the buttons. Must have two tag lines: "it pays to share" and "get paid to share music" Please include the elements, such as login, join, etc... that are in the comp that you can download. Obviously I don't want it to look like what I already have, except that it must have a container that holds the video. The container that holds the video has to have the same aspect ratio that kobrastream uses for it's embed codes. You can find this ratio by checking any kobrastream video embed code, they have a custom size tool which lets you play with the sizes. Any question, pls contact thanks.
Nice to have
• unlike the existing comp, it can have white space. Just looking for a good modern theme with a cool logo. Jquery style themes might be nice... Also, think along the lines of a cool techy feel for mobile...

This is a cool image, but obviously don't get too close to it because it belongs to another music site:

http://kpnoverbyte2011.files.brindlehost.com/2012/03/capture-2012-03-28-at-12-02-36-pm.png?w=194

```html
<!DOCTYPE html>
<html lang="en">
<head>
<meta charset="utf-8">
<title>vellar — it pays to share</title>
<link href="https://fonts.googleapis.com/css2?family=Comfortaa:wght@400;700&family=Special+Elite&family=Arimo:ital,wght@0,400;0,700;1,400&display=swap" rel="stylesheet">
<style>
  :root {
    --page: #e8e8e8;
    --page-light: #f6f6f6;
    --ink: #222;
    --muted: #888;
    --brand: #2b7fe6;
    --nav-active: #2f86f0;
    --login: #4a4a4a;
    --join: #2e5a75;
    --frame: #111;
    --video-sky: #6fb6d9;
    --video-ground: #a88a4a;
    --highlight: #fdfcc2;
    --card: #fff;
    --link: #2a66b8;
  }
  * { box-sizing: border-box; margin: 0; padding: 0; }
  html, body { width: 1200px; height: 1039px; overflow: hidden; }
  body {
    background: radial-gradient(ellipse at 50% 35%, var(--page-light) 0%, var(--page) 70%);
    font-family: "Arimo", Arial, sans-serif;
    color: var(--ink);
    position: relative;
  }
  .brand { position: absolute; left: 156px; top: 16px; }
  .brand-name {
    font-family: "Comfortaa", sans-serif; font-weight: 700;
    font-size: 78px; line-height: 1; color: var(--brand); letter-spacing: -2px;
  }
  .brand-tagline {
    font-family: "Comfortaa", sans-serif; font-size: 30px; color: #555;
    margin-top: 14px; margin-left: 8px;
  }
  .account { position: absolute; top: 56px; left: 925px; display: flex; gap: 10px; }
  .account a {
    font-family: "Special Elite", monospace; font-size: 22px; color: #fff;
    text-decoration: none; padding: 4px 8px; border: 2px solid #fff;
    box-shadow: 0 0 0 1px #bbb;
  }
  .account .login { background: var(--login); }
  .account .join { background: var(--join); }

  .dancer {
    position: absolute; left: 136px; top: 168px; width: 140px; height: 140px;
    background: radial-gradient(circle at 50% 40%, #2a2a2a 0%, #444 55%, transparent 72%);
  }
  .main-nav {
    position: absolute; left: 138px; top: 178px; width: 932px; height: 46px;
    background: #fdfdfd; box-shadow: 0 3px 6px rgba(0,0,0,.25);
  }
  .main-nav ul { list-style: none; position: relative; height: 100%; }
  .main-nav li {
    position: absolute; top: 0; height: 100%; display: flex; align-items: center;
    font-family: "Special Elite", monospace; font-size: 21px; color: #333;
  }
  .main-nav li.active { background: var(--nav-active); color: #fff; padding: 0 26px; }

  .player-frame {
    position: absolute; left: 258px; top: 266px; width: 534px; height: 394px;
    border: 16px solid var(--frame); border-radius: 36px; background: var(--frame);
  }
  .player-frame::after {
    content: ""; position: absolute; right: -30px; bottom: -28px; width: 14px; height: 70px;
    background: var(--frame); border-radius: 6px;
  }
  .video {
    position: absolute; left: 19px; top: 18px; width: 466px; height: 312px;
    background: linear-gradient(180deg, var(--video-sky) 0%, #8cb8c4 35%, #7d6a55 60%, #4a3a33 100%);
  }
  .play {
    position: absolute; left: 178px; top: 100px; width: 116px; height: 116px;
    border-radius: 50%; background: rgba(60,50,40,.7);
    display: flex; align-items: center; justify-content: center;
  }
  .video-stats {
    position: absolute; left: 19px; top: 330px; width: 466px; height: 22px;
    font-size: 11px; font-style: italic; color: #aaa; text-align: right; padding: 4px 6px;
  }
  .video-stats span { color: #5a9ae6; }
  .track-title { position: absolute; left: 167px; top: 676px; font-weight: 700; font-size: 17px; }
  .track-meta { position: absolute; left: 167px; top: 704px; font-size: 11px; font-style: italic; color: #666; }
  .track-meta a { color: var(--link); text-decoration: none; }
  .download {
    position: absolute; left: 659px; top: 688px; width: 122px; height: 28px;
    background: linear-gradient(#555, #222); border-radius: 14px; color: #fff;
    font-weight: 700; font-size: 15px; display: flex; align-items: center; justify-content: center; gap: 8px;
  }

  .playlist { position: absolute; left: 836px; top: 262px; width: 230px; }
  .playlist .arrow { display: block; margin: 0 auto; }
  .playlist ol { list-style: none; margin: 10px 0; }
  .clip {
    height: 76px; background: var(--card); margin-bottom: 17px; padding: 5px;
    display: flex; gap: 12px; box-shadow: 0 1px 3px rgba(0,0,0,.2);
  }
  .clip.current { background: var(--highlight); }
  .clip-thumb { width: 117px; height: 66px; position: relative; flex: none; }
  .clip-thumb b {
    position: absolute; right: 4px; bottom: 3px; color: #fff; font-size: 11px; font-weight: 700;
  }
  .clip h3 { font-size: 13px; line-height: 16px; font-weight: 400; margin-top: 3px; }
  .clip p { font-size: 11px; color: var(--muted); line-height: 15px; }

  .slogan-band {
    position: absolute; left: 120px; top: 768px; width: 960px; height: 144px;
  }
  .slogan {
    position: absolute; left: 0; top: 814px; width: 1200px; text-align: center;
    font-family: "Comfortaa", sans-serif; font-size: 30px; color: #333;
  }
  .social { position: absolute; top: 916px; left: 0; width: 1200px; display: flex; justify-content: center; gap: 8px; list-style: none; }
  .social li {
    display: flex; align-items: center; gap: 5px; font-size: 11px; color: #444;
    background: #fff; border: 1px solid #ccc; border-radius: 6px; padding: 10px 7px;
  }
  .social i { width: 12px; height: 12px; border-radius: 2px; display: block; }
  .copyright { position: absolute; top: 978px; width: 1200px; text-align: center; font-size: 12px; color: #444; }
</style>
</head>
<body>
  <header class="brand">
    <div class="brand-name">vellar</div>
    <div class="brand-tagline">it pays to share</div>
  </header>
  <nav class="account"><a class="login" href="#">LOGIN</a><a class="join" href="#">JOIN</a></nav>

  <div class="dancer" role="img" aria-label="Silhouette of a dancing figure"></div>
  <nav class="main-nav">
    <ul>
      <li class="active" style="left:211px">HOME</li>
      <li style="left:336px">ABOUT</li>
      <li style="left:442px">TERMS</li>
      <li style="left:547px">PRIVACY</li>
      <li style="left:676px">SETTINGS</li>
      <li style="left:814px">SUPPORT</li>
    </ul>
  </nav>

  <section class="player-frame">
    <div class="video" role="img" aria-label="Video still of a band posing outdoors">
      <div class="play"><svg width="50" height="56" viewBox="0 0 50 56"><path d="M4 2 L48 28 L4 54 Z" fill="#e0c64a"/></svg></div>
    </div>
    <div class="video-stats">10,456 <span>Vellars</span> &nbsp;&nbsp;&nbsp; 11,291 <span>Fans</span></div>
  </section>
  <h1 class="track-title">Vampire Lovae</h1>
  <p class="track-meta">Uploaded by <a href="#">officialvarro</a> on Sep 10, 2011</p>
  <a class="download"><svg width="16" height="14" viewBox="0 0 16 14"><path d="M6 0h4v5h3l-5 5-5-5h3z M0 11h16v3H0z" fill="#fff"/></svg>Download</a>

  <aside class="playlist">
    <svg class="arrow" width="28" height="12" viewBox="0 0 28 12"><path d="M0 12 L14 0 L28 12Z" fill="#bbb"/></svg>
    <ol>
      <li class="clip current"><div class="clip-thumb" role="img" aria-label="Band standing in a row" style="background:linear-gradient(#ddd,#444)"><b>2:05</b></div><div><h3>Neque porro quisquam</h3><p>b4 lbus067<br>79,345 views</p></div></li>
      <li class="clip"><div class="clip-thumb" role="img" aria-label="Concert stage with blue lasers" style="background:linear-gradient(#1d3fa8,#5fb3f0)"><b>10:46</b></div><div><h3>Neque porro quisquam</h3><p>b4 lbus067<br>79,345 views</p></div></li>
      <li class="clip"><div class="clip-thumb" role="img" aria-label="Club dancer under purple light" style="background:linear-gradient(#5a1e6a,#c04fb8)"><b>6:30</b></div><div><h3>Neque porro quisquam</h3><p>b4 lbus067<br>79,345 views</p></div></li>
      <li class="clip"><div class="clip-thumb" role="img" aria-label="Performer on a warm-lit stage" style="background:linear-gradient(#3a1a10,#b0643a)"><b>3:36</b></div><div><h3>Neque porro quisquam</h3><p>b4 lbus067<br>79,345 views</p></div></li>
    </ol>
    <svg class="arrow" width="28" height="12" viewBox="0 0 28 12"><path d="M0 0 L14 12 L28 0Z" fill="#bbb"/></svg>
  </aside>

  <svg class="slogan-band" viewBox="0 0 960 144" preserveAspectRatio="none">
    <path d="M0 22 Q480 -10 960 22 Q480 10 0 22Z" fill="#d4d4d4"/>
    <path d="M0 122 Q480 110 960 122 Q480 154 0 122Z" fill="#d4d4d4"/>
  </svg>
  <p class="slogan">get paid to share music</p>

  <ul class="social">
    <li><i style="background:#3b5a9a"></i>Plumora</li>
    <li><i style="background:#3bb0e0"></i>Zendrol</li>
    <li><i style="background:#1e5080"></i>Burrowly</li>
    <li><i style="background:#f06a1c"></i>Scribbox</li>
    <li><i style="background:#c8101a"></i>Tunefold</li>
    <li><i style="background:#d62a22"></i>kobrastream</li>
  </ul>
  <p class="copyright">© 2012 Kindred Share Media. All Rights Reserved.</p>
</body>
</html>
```